FLYER: Human Factors in Traffic Crashes - Analysis of Drivers' Responses - training

We are hosting a class in Australia 30, November to 4, December 2020. I would like to have a flyer designed to "sell" the class with description of course topics. I have uploaded a flyer I started on my own but I want it to be professional. Dr. Pelloway only gets to AU every 3-5 years to teach from the US. I would like to have some type of roadway scenery, prefer a nighttime scene.

Target Market(s)

Accident reconstructionists and engineers, police reconstructionists.

Font styles to use
Serif

Colors
fec214

Requirements
Must have
• Name of course and course topics, location of course, price, website and contact information.
Nice to have
• Some type of roadway background, possibly a nighttime scene on a roadway.

```html
<!DOCTYPE html>
<html lang="en">
<head>
<meta charset="utf-8">
<title>Human Factors in Traffic Crashes – Flyer</title>
<link href="https://fonts.googleapis.com/css2?family=Oswald:wght@400;500;700&family=Open+Sans:wght@400;600;700&display=swap" rel="stylesheet">
<style>
  :root{
    --yellow:#fec214;
    --ink:#1b1b1b;
    --charcoal:#262626;
    --panel:#3a3a3a;
    --cell:#6a6a6a;
    --strip:#4b4b4b;
    --white:#ffffff;
    --paper:#e4e4e4;
    --muted:#bdbdbd;
  }
  *{box-sizing:border-box;margin:0;padding:0}
  html,body{width:1200px;height:2400px;overflow:hidden}
  body{background:var(--paper);font-family:"Open Sans",sans-serif;position:relative}
  .flyer{position:absolute;left:100px;top:493px;width:1000px;height:1414px;background:var(--ink);overflow:hidden;box-shadow:0 10px 40px rgba(0,0,0,.25)}
  .main{position:absolute;left:0;top:0;width:600px;height:1344px;padding:44px 0 0 44px;
    background:linear-gradient(180deg,#111 0%,var(--charcoal) 100%)}
  .brand{display:flex;align-items:center;gap:16px;height:110px}
  .brand-mark{width:28px;height:28px;background:var(--yellow);flex:none}
  .brand-name{font-family:"Oswald",sans-serif;font-weight:700;color:var(--white);font-size:34px;line-height:1;letter-spacing:1px;text-transform:uppercase}
  .headline{margin-top:56px;font-family:"Oswald",sans-serif;font-weight:700;text-transform:uppercase;line-height:.98}
  .headline .line-a{display:block;color:var(--yellow);font-size:58px}
  .headline .line-b{display:block;color:var(--yellow);font-size:94px;margin-top:4px}
  .headline .line-c{display:block;color:var(--white);font-size:60px;margin-top:4px}
  .class-tag{display:flex;margin-top:24px;margin-right:40px;font-family:"Oswald",sans-serif;font-weight:500;font-size:30px;text-transform:uppercase}
  .class-tag .label{background:var(--yellow);color:var(--ink);padding:6px 20px}
  .class-tag .place{background:var(--panel);color:var(--yellow);padding:6px 24px;flex:1}
  .presenter{margin-top:30px;margin-right:40px;color:var(--white);font-family:"Oswald",sans-serif;font-size:27px;line-height:1.3;text-transform:uppercase}
  .presenter span{display:block;font-family:"Open Sans",sans-serif;font-weight:600;font-size:20px;text-transform:none}
  .details{margin-top:26px;margin-right:40px;display:grid;grid-template-columns:150px 1fr 1fr;gap:6px}
  .details .key{background:var(--panel);color:var(--white);font-family:"Oswald",sans-serif;font-size:24px;text-transform:uppercase;padding:14px 16px;display:flex;align-items:center}
  .details .val{background:var(--cell);color:var(--white);font-size:18px;font-weight:600;padding:14px 16px;line-height:1.35;display:flex;align-items:center}
  .details .wide{grid-column:2 / 4}
  .note{margin-top:22px;margin-right:60px;color:var(--muted);font-size:17px;line-height:1.45}
  .register{margin-top:24px;margin-right:60px;background:var(--yellow);padding:18px 22px;color:var(--ink)}
  .register h3{font-family:"Oswald",sans-serif;font-weight:700;font-size:28px;text-transform:uppercase;margin-bottom:8px}
  .register p{font-size:17px;font-weight:600;line-height:1.45}
  .side{position:absolute;left:600px;top:0;width:400px;height:1344px;background:var(--yellow);padding:40px 28px 0 28px}
  .photo{display:block;width:344px;height:260px;background:linear-gradient(160deg,#7fc4e6 0%,#2f88b5 45%,#2e6b3a 80%,#3d5d2a 100%)}
  .topics-title{margin-top:40px;font-family:"Oswald",sans-serif;font-weight:700;font-size:34px;color:var(--ink);text-transform:uppercase;border-bottom:3px solid var(--ink);padding-bottom:8px}
  .topics{list-style:none;margin-top:18px}
  .topics li{position:relative;padding-left:26px;margin-bottom:22px;font-size:20px;font-weight:600;line-height:1.35;color:var(--ink)}
  .topics li::before{content:"";position:absolute;left:0;top:9px;width:11px;height:11px;background:var(--ink)}
  .footer-strip{position:absolute;left:0;bottom:0;width:1000px;height:70px;background:var(--strip);color:var(--white);
    display:flex;align-items:center;justify-content:center;gap:14px;font-family:"Oswald",sans-serif;font-size:25px;letter-spacing:.5px;text-transform:uppercase}
</style>
</head>
<body>
  <article class="flyer">
    <section class="main">
      <div class="brand">
        <span class="brand-mark"></span>
        <span class="brand-name">Kerbline Research</span>
      </div>

      <h1 class="headline">
        <span class="line-a">Human Factors<br>in Traffic Crashes</span>
        <span class="line-b">Analysis of</span>
        <span class="line-c">Drivers' Responses</span>
      </h1>

      <div class="class-tag"><span class="label">Open Class:</span><span class="place">Manly NSW</span></div>

      <p class="presenter">Presented by: Alan Pelloway Ph.D.<span>Driver behaviour researcher and educator</span></p>

      <div class="details">
        <div class="key">Location:</div>
        <div class="val wide">Sydney Harbour Pavilion, North Head, Manly NSW 2095</div>
        <div class="key">Course Fee:</div>
        <div class="val">$1,795 AU</div>
        <div class="val">30 Nov – 4 Dec 2020</div>
      </div>

      <p class="note">It has been 5 years since Dr. Pelloway has come to our beach, don't miss out on this year's class. Seats are limited.</p>

      <div class="register">
        <h3>Register on our website:</h3>
        <p>www.kerblineresearch.example<br>training@kerblineresearch.example<br>+61 2 5550 1234</p>
      </div>
    </section>

    <aside class="side">
      <div class="photo" role="img" aria-label="Aerial photo of a harbour bay with ferries, blue water and green headland"></div>
      <h2 class="topics-title">Course Topics</h2>
      <ul class="topics">
        <li>Human response time and driver decisions</li>
        <li>Hazard perception and recognition</li>
        <li>Expectation and driver attention</li>
        <li>Night visibility and conspicuity</li>
        <li>Pedestrian and cyclist detection</li>
        <li>Research on driver braking</li>
        <li>Steering, braking and evasive responses</li>
        <li>Distraction and impairment effects</li>
        <li>Speed and distance judgment</li>
        <li>Applying research to crash reconstruction</li>
      </ul>
    </aside>

    <footer class="footer-strip"><span>Visit www.kerblineresearch.example/about/</span><span>to learn more about Dr. Pelloway</span></footer>
  </article>
</body>
</html>
```